" a empresa trabalha na area de divulgação, e marketing usando a ferramenta instagram e facebook, usando o perfil de seus clientes, transformando em e-commerce, é tambem atua na area de vendas de paineis de led em acrilico "

```html
<!DOCTYPE html>
<html lang="pt">
<head>
<meta charset="UTF-8">
<title>Vantix – Cartão de visita</title>
<link rel="stylesheet" href="https://fonts.googleapis.com/css2?family=Montserrat:wght@500;600&display=swap">
<style>
  :root {
    --page-bg: #dfe3e8;
    --card-face: #f3f4f6;
    --band-dark: #2a2a2e;
    --accent-red: #c8202f;
    --accent-deep: #7a1022;
    --brand-ink: #8a1838;
    --tagline-ink: #b3203a;
  }
  * { margin: 0; padding: 0; box-sizing: border-box; }
  html, body {
    width: 1200px;
    height: 1200px;
    overflow: hidden;
    background: var(--page-bg);
  }
  .canvas {
    position: relative;
    width: 1200px;
    height: 1200px;
  }
  .business-card {
    position: absolute;
    left: 100px;
    top: 305px;
    width: 1000px;
    height: 590px;
    border-radius: 22px;
    overflow: hidden;
    background: var(--card-face);
    box-shadow: 0 20px 50px rgba(0, 0, 0, 0.18);
  }
  .card-graphic {
    position: absolute;
    inset: 0;
    width: 100%;
    height: 100%;
  }
  .brand-block {
    position: absolute;
    left: 190px;
    top: 230px;
    display: flex;
    flex-direction: column;
    align-items: center;
    font-family: "Montserrat", sans-serif;
  }
  .brand-mark {
    width: 58px;
    height: 58px;
    background: var(--brand-ink);
    margin-bottom: 36px;
  }
  .brand-name {
    font-size: 92px;
    font-weight: 500;
    letter-spacing: 4px;
    line-height: 1;
    color: var(--brand-ink);
  }
  .brand-tagline {
    margin-top: 14px;
    font-size: 17px;
    font-weight: 600;
    letter-spacing: 0.6px;
    color: var(--tagline-ink);
    white-space: nowrap;
  }
</style>
</head>
<body>
  <main class="canvas">
    <section class="business-card">
      <svg class="card-graphic" viewBox="0 0 1000 590" preserveAspectRatio="none" aria-hidden="true">
        <defs>
          <linearGradient id="red-corner" x1="0" y1="0" x2="1" y2="1">
            <stop offset="0" stop-color="var(--accent-red)"/>
            <stop offset="1" stop-color="var(--accent-deep)"/>
          </linearGradient>
        </defs>
        <path class="dark-band" d="M 880 0 C 975 260 720 560 260 590 L 1000 590 L 1000 0 Z" fill="var(--band-dark)"/>
        <path class="red-edge" d="M 880 0 C 975 260 720 560 260 590" fill="none" stroke="var(--accent-red)" stroke-width="5"/>
        <path class="red-corner" d="M 1000 210 C 965 420 830 555 640 590 L 1000 590 Z" fill="url(#red-corner)"/>
      </svg>
      <div class="brand-block">
        <div class="brand-mark"></div>
        <h1 class="brand-name">VANTIX</h1>
        <p class="brand-tagline">MARKETING DIGITAL E COMUNICAÇÃO VISUAL</p>
      </div>
    </section>
  </main>
</body>
</html>
```